Email Banner - TevonQuarry.com

I need an email banner created for my website: Tevonquarry.com.
The logos are attatched here and an example of an email banner we have used in the past is also attatched. Please keep the tagline: "Essential Whitepapers for Business Professionals" - The logos are in the framebazaar zip folder.

Tevonquarry

```html
<!DOCTYPE html>
<html lang="en">
<head>
<meta charset="UTF-8">
<title>Tevonquarry Email Banner</title>
<link href="https://fonts.googleapis.com/css2?family=Montserrat:wght@400;600;700&display=swap" rel="stylesheet">
<style>
  :root {
    --navy: #263381;
    --blue: #3a6cf5;
    --sky: #8fb0fb;
    --white: #ffffff;
    --page: #fefefe;
    --brand-ink: #2344b8;
  }
  html, body {
    margin: 0;
    padding: 0;
    width: 1200px;
    height: 1000px;
    overflow: hidden;
    background: var(--page);
    font-family: "Montserrat", Arial, sans-serif;
  }
  .canvas {
    position: relative;
    width: 1200px;
    height: 1000px;
  }
  .email-banner {
    position: absolute;
    left: 195px;
    top: 411px;
    width: 811px;
    height: 127px;
    background: var(--white);
    overflow: hidden;
  }
  .banner-shapes {
    position: absolute;
    inset: 0;
    width: 811px;
    height: 127px;
  }
  .cta-label {
    position: absolute;
    left: 16px;
    top: 8px;
    margin: 0;
    font-size: 10.5px;
    font-weight: 700;
    color: var(--white);
    letter-spacing: 0.1px;
  }
  .tagline {
    position: absolute;
    left: 75px;
    top: 35px;
    margin: 0;
    color: var(--white);
    font-size: 27px;
    line-height: 29px;
    font-weight: 400;
    letter-spacing: 0.6px;
  }
  .tagline .lead-in {
    display: block;
  }
  .tagline .second-line {
    display: block;
    padding-left: 2px;
    font-size: 19px;
  }
  .tagline strong {
    font-weight: 700;
    font-size: 25px;
    margin-left: 8px;
    letter-spacing: 0.4px;
  }
  .brand {
    position: absolute;
    left: 612px;
    top: 30px;
    width: 160px;
    text-align: center;
  }
  .brand-dot {
    display: block;
    width: 30px;
    height: 30px;
    margin: 0 auto 6px;
    border-radius: 50%;
    background: var(--sky);
  }
  .brand-name {
    margin: 0;
    font-size: 22px;
    font-weight: 600;
    color: var(--brand-ink);
    letter-spacing: -0.3px;
  }
</style>
</head>
<body>
<div class="canvas">
  <section class="email-banner">
    <svg class="banner-shapes" viewBox="0 0 811 127" aria-hidden="true">
      <path fill="var(--sky)" d="M0,0 H700 C615,3 545,70 470,96 C390,121 285,128 230,127 C130,126 40,110 0,84 Z"/>
      <path fill="var(--blue)" d="M0,0 H668 C590,3 525,70 448,96 C370,120 280,127 230,126 C130,125 40,104 0,79 Z"/>
      <path fill="var(--navy)" d="M0,0 H640 C560,3 500,70 420,96 C350,118 270,127 230,126 C130,124 40,100 0,72 Z"/>
      <path fill="var(--blue)" d="M0,0 H122 C104,0 98,8 93,16 C87,26 82,29 72,29 H18 C8,29 0,32 0,38 Z"/>
      <path fill="var(--sky)" d="M811,86 C811,112 790,127 757,127 H811 Z"/>
    </svg>
    <p class="cta-label">CLICK HERE</p>
    <h1 class="tagline">
      <span class="lead-in">Essential Whitepapers</span>
      <span class="second-line">for<strong>Business Professionals</strong></span>
    </h1>
    <div class="brand">
      <span class="brand-dot"></span>
      <p class="brand-name">Tevonquarry</p>
    </div>
  </section>
</div>
</body>
</html>
```